Velora Pedalworks

We are a new start up company selling (online) innovative cycling products.
Being a new player in the market a modern eye catching logo would be good.
Initially selling safety tail lights with blinkers & modern designed cycling gloves and eventually extending our range into cycling clothing. Many of our products will have a safety theme.

Please see logo attached.

Reason: I have extended deadline because i have just received the Logo to be used.

Target Market(s)

We will be target marketing to the young 20-30year old trendy commuter cyclists to the 40 - 60 year old weekend road riders with there immaculate color coordinated road bikes & clothing.

Industry/Entity Type

Safety

Requirements
Must have
• Name: Mavin Tolby
Line for Mobile No. 0438 261 905
Line for email Address: mavin@velorapedalworks.example.com.au
3 Lines for Postal Address: PO Box 3862
Wattle Crest Corner
NSW 2174
Website: www.velorapedalworks.example.com.au

```html
<!DOCTYPE html>
<html lang="en">
<head>
<meta charset="utf-8">
<title>Velora Pedalworks – Business Card</title>
<link href="https://fonts.googleapis.com/css2?family=Open+Sans:wght@400;600;700&display=swap" rel="stylesheet">
<style>
  :root {
    --ink: #232323;
    --orange: #d9822b;
    --paper: #ffffff;
    --backdrop: #e4e4e4;
    --light-text: #ffffff;
  }
  * { box-sizing: border-box; margin: 0; padding: 0; }
  html, body { width: 1200px; height: 720px; overflow: hidden; }
  body {
    background: var(--backdrop);
    font-family: "Open Sans", Arial, sans-serif;
    display: flex;
    align-items: center;
    justify-content: center;
    gap: 40px;
  }
  .card {
    position: relative;
    width: 540px;
    height: 310px;
    background: var(--paper);
    overflow: hidden;
    box-shadow: 0 6px 18px rgba(0,0,0,.18);
  }

  /* Front: brand name */
  .card-front { display: flex; align-items: center; justify-content: center; }
  .brand { display: flex; align-items: center; gap: 12px; }
  .brand-name { font-weight: 600; color: var(--ink); letter-spacing: -0.5px; }
  .brand-dot { border-radius: 50%; background: var(--orange); }
  .card-front .brand-name { font-size: 36px; }
  .card-front .brand-dot { width: 16px; height: 16px; }

  /* Back: details */
  .header-shape { position: absolute; inset: 0; width: 540px; height: 310px; }
  .card-back .brand { position: absolute; left: 32px; top: 68px; }
  .card-back .brand-name { font-size: 22px; }
  .card-back .brand-dot { width: 10px; height: 10px; }
  .holder-name {
    position: absolute; left: 262px; top: 14px;
    font-size: 26px; font-weight: 700; color: var(--light-text);
  }
  .holder-role {
    position: absolute; right: 24px; top: 68px;
    font-size: 18px; font-weight: 700; color: var(--light-text);
  }
  .contact-list { position: absolute; left: 40px; right: 0; top: 118px; list-style: none; }
  .contact-row {
    display: flex; align-items: center; gap: 10px;
    background: var(--orange); color: var(--light-text);
    border-radius: 8px 0 0 8px;
    height: 26px; padding-left: 10px; margin-bottom: 6px;
    font-size: 13px; font-weight: 600;
  }
  .contact-row.address { height: 54px; align-items: flex-start; padding-top: 4px; line-height: 15.5px; }
  .contact-icon { width: 14px; height: 14px; flex: none; }
  .address .contact-icon { margin-top: 1px; }
  .footer-line {
    position: absolute; left: 0; right: 0; bottom: 24px; height: 3px; background: var(--orange);
  }
  .footer-band {
    position: absolute; left: 0; right: 0; bottom: 0; height: 18px; background: var(--ink);
  }
</style>
</head>
<body>

  <section class="card card-back" aria-label="Business card, details side">
    <svg class="header-shape" viewBox="0 0 540 310" aria-hidden="true">
      <path d="M240 0 H540 V100 H380 C350 100 352 58 322 58 H240 Z" fill="var(--ink)"/>
      <path d="M380 56 H540 V100 H380 C360 100 356 56 380 56 Z" fill="var(--orange)" transform="translate(0,0)"/>
    </svg>
    <div class="brand">
      <span class="brand-name">Velora Pedalworks</span>
      <span class="brand-dot"></span>
    </div>
    <p class="holder-name">Mavin Tolby</p>
    <p class="holder-role">Owner</p>

    <ul class="contact-list">
      <li class="contact-row">
        <svg class="contact-icon" viewBox="0 0 14 14" aria-hidden="true"><rect x="3.5" y="1" width="7" height="12" rx="1.5" fill="none" stroke="#fff" stroke-width="1.4"/><circle cx="7" cy="10.6" r=".9" fill="#fff"/></svg>
        <span>0438 261 905</span>
      </li>
      <li class="contact-row">
        <svg class="contact-icon" viewBox="0 0 14 14" aria-hidden="true"><rect x="1" y="3" width="12" height="8.5" fill="none" stroke="#fff" stroke-width="1.3"/><path d="M1 3 L7 8 L13 3" fill="none" stroke="#fff" stroke-width="1.3"/></svg>
        <span>mavin@velorapedalworks.example.com.au</span>
      </li>
      <li class="contact-row">
        <svg class="contact-icon" viewBox="0 0 14 14" aria-hidden="true"><rect x="1" y="2" width="12" height="8" fill="none" stroke="#fff" stroke-width="1.3"/><path d="M5 13 H9 M7 10 V13" stroke="#fff" stroke-width="1.3"/></svg>
        <span>www.velorapedalworks.example.com.au</span>
      </li>
      <li class="contact-row address">
        <svg class="contact-icon" viewBox="0 0 14 14" aria-hidden="true"><path d="M7 13.5 C4 9.5 2.5 7.5 2.5 5.2 A4.5 4.5 0 0 1 11.5 5.2 C11.5 7.5 10 9.5 7 13.5 Z" fill="#fff"/><circle cx="7" cy="5.2" r="1.6" fill="var(--orange)"/></svg>
        <span>PO Box 3862<br>Wattle Crest Corner<br>NSW 2174</span>
      </li>
    </ul>

    <div class="footer-line"></div>
    <div class="footer-band"></div>
  </section>

  <section class="card card-front" aria-label="Business card, brand side">
    <div class="brand">
      <span class="brand-name">Velora Pedalworks</span>
      <span class="brand-dot"></span>
    </div>
  </section>

</body>
</html>
```